Logo and website for new private wealth management business

This project is for a new company website and logo. The name of the firm is Harborline Estate Partners, LLC. We are a wealth management firm offering customized financial planning and investment management services to high net worth and ultra high net worth individuals and families. I want the website to feel contemporary but convey a feeling of sophistication and prestige.
www.tolvanridgeholdings.example and www.qnfunds.example are both good reference websites.
My clients will consist of wealthy individuals and families. I have existing clients in their 50s - 70s, but I also intend to target younger business owners and entrepreneurs in their 30s -50s.

Target Market(s)

Business owners, entrepreneurs and corporate executives. Many existing clients are in their 60s and 70s, but intend to also attract a younger clientele in their 30s - 50s.

Industry/Entity Type

Wealth management, investment advisory, financial planning

Coding

Coded - Design and coding required

Colors
0054AA
0677BA
7BADD7
CADEEF
E8F1F8
0094D4
00A9DD
6FCCEA
C7EBF8
E9F6FB
00AB8E
00BBA5
67D7C9
C6EFE9
E9F9F6
EE7325
F08F49
F5BC92
FAE3D3
FDF4ED

Requirements
Must have
• Should use blue as the main color theme. Should have an About, Services, Our Clients, FAQ, and Contact sections
Should not have
• Should not have pictures of people as the background.

```html
<!DOCTYPE html>
<html lang="en">
<head>
<meta charset="utf-8">
<title>Harborline Estate Partners, LLC</title>
<link href="https://fonts.googleapis.com/css2?family=Poppins:wght@300;400;500;600&display=swap" rel="stylesheet">
<style>
:root{
  --blue:#0677BA;
  --navy:#0b1a7a;
  --ink:#1b1b1b;
  --text:#2a2a2a;
  --panel:#fafafa;
  --paper:#f1f1f1;
  --footer:#222222;
  --white:#ffffff;
}
*{margin:0;padding:0;box-sizing:border-box}
html,body{width:1200px;height:3286px;overflow:hidden}
body{position:relative;font-family:'Poppins',sans-serif;color:var(--text);background:var(--white)}

/* hero */
.hero{position:absolute;left:0;top:0;width:1200px;height:640px;background:linear-gradient(180deg,#3a9ad6 0%,#3573c4 50%,#3b55ae 100%)}
.hero-edge{position:absolute;left:0;top:500px;width:1200px;height:160px}
.brand{position:absolute;left:89px;top:34px;display:flex;align-items:center;gap:10px;color:var(--white)}
.brand-mark{width:30px;height:30px;background:var(--white)}
.brand-name{font-weight:600;font-size:16px;line-height:19px;letter-spacing:.3px}
.nav{position:absolute;top:48px;left:609px;display:flex;gap:23px;color:var(--white);font-weight:500;font-size:16px}
.nav-rule{position:absolute;left:89px;top:96px;width:1039px;height:1px;background:rgba(255,255,255,.6)}
.hero-kicker{position:absolute;top:245px;width:1200px;text-align:center;color:var(--white);font-size:26px;font-weight:400}
.hero-title{position:absolute;top:288px;width:1200px;text-align:center;color:var(--white);font-size:39px;font-weight:500;letter-spacing:.5px}
.scroll{position:absolute;top:436px;left:578px;width:44px;height:44px}
.scroll-label{position:absolute;top:487px;width:1200px;text-align:center;color:var(--white);font-size:17px}

/* buttons */
.btn{position:absolute;height:43px;background:var(--blue);color:var(--white);font-size:15px;font-weight:400;display:flex;align-items:center;justify-content:center;gap:10px}
.btn svg{width:18px;height:14px}

/* about */
.about-title{position:absolute;left:221px;top:704px;font-size:30px;font-weight:500;color:var(--blue)}
.about-copy{position:absolute;left:585px;top:701px;width:465px;font-size:15.5px;line-height:26px;color:var(--ink)}

/* services */
.dotmap{position:absolute;left:0;top:940px;width:1080px;height:380px;background:radial-gradient(ellipse at 18% 40%,rgba(232,232,232,.6),rgba(255,255,255,0) 60%)}
.section-head{position:absolute;width:1200px;text-align:center;font-size:32px;font-weight:500;color:var(--ink)}
.section-head .rule{display:inline-block;width:62px;height:2px;background:currentColor;vertical-align:middle;margin:0 20px}
.services-intro{position:absolute;top:1086px;width:1200px;text-align:center;font-size:15.5px;line-height:26px;color:var(--ink)}
.services-panel{position:absolute;left:0;top:1375px;width:1074px;height:391px;background:var(--panel)}
.photo{position:absolute;width:196px;height:196px;border-radius:50%;border:3px solid var(--blue)}
.service-title{position:absolute;width:260px;text-align:center;font-size:20px;font-weight:500;color:var(--ink)}
.service-copy{position:absolute;width:260px;text-align:center;font-size:15.5px;line-height:26px;color:var(--ink)}

/* why */
.why{position:absolute;left:0;top:1640px;width:1200px;height:910px}
.why-label{position:absolute;color:var(--white);font-size:16.5px;font-weight:500}
.why-copy{position:absolute;color:var(--white);font-size:12px;line-height:17.5px;width:135px}

/* contact */
.contact-bg{position:absolute;left:0;top:2300px;width:1200px;height:653px;background:var(--paper);z-index:-1}
.contact-title{position:absolute;left:122px;top:2543px;font-size:30px;font-weight:500;color:var(--ink)}
.contact-copy{position:absolute;left:122px;top:2596px;width:340px;font-size:14px;line-height:20px;color:var(--ink)}
.contact-co{position:absolute;left:122px;top:2684px;font-size:20px;font-weight:500;color:var(--ink)}
.info{position:absolute;left:121px;display:flex;align-items:center;gap:14px;font-size:14px;color:var(--ink)}
.info svg{width:18px;height:18px}
.field{position:absolute;background:var(--white);font-size:17px;color:#444;padding:10px 18px}

/* footer */
.footer-band{position:absolute;left:0;top:2953px;width:1200px;height:8px;background:var(--blue)}
.footer{position:absolute;left:0;top:2961px;width:1200px;height:325px;background:var(--footer);color:var(--white)}
.footer-about{position:absolute;left:121px;top:78px;width:235px;font-size:13.5px;line-height:20px}
.footer-co{position:absolute;left:462px;top:48px;font-size:13.5px;font-weight:500}
.footer-info{position:absolute;left:461px;display:flex;align-items:center;gap:14px;font-size:13.5px}
.footer-info svg{width:17px;height:17px}
.footer-nav{position:absolute;left:803px;top:46px;font-size:13.5px;line-height:24px;font-weight:500}
.social{position:absolute;top:54px;width:23px;height:23px;border-radius:50%;border:2px solid var(--white)}
.footer-rule{position:absolute;left:121px;top:224px;width:953px;height:1px;background:#444}
.copyright{position:absolute;top:252px;width:1200px;text-align:center;font-size:11.5px}
</style>
</head>
<body>

<!-- hero -->
<header class="hero" role="img" aria-label="Abstract flowing blue wave pattern"></header>
<svg class="hero-edge" viewBox="0 500 1200 160" width="1200" height="160" aria-hidden="true">
  <polygon points="0,628 1200,510 1200,552 0,640" fill="#1493d6"/>
  <polygon points="0,634 1200,552 1200,570 0,640" fill="#0b1a7a"/>
  <polygon points="0,640 1200,570 1200,660 0,660" fill="#ffffff"/>
</svg>
<div class="brand"><span class="brand-mark"></span><span class="brand-name">HARBORLINE ESTATE<br>PARTNERS, LLC</span></div>
<nav class="nav"><span>HOME</span><span>ABOUT</span><span>SERVICE</span><span>OUR CLIENTS</span><span>FAQ</span><span>CONTACT</span></nav>
<div class="nav-rule"></div>
<p class="hero-kicker">WELCOME TO</p>
<h1 class="hero-title">HARBORLINE ESTATE PARTNERS, LLC</h1>
<svg class="scroll" viewBox="0 0 44 44" aria-hidden="true"><circle cx="22" cy="22" r="21" fill="none" stroke="#fff" stroke-width="1.5"/><path d="M22 12v19M15 24l7 7 7-7" fill="none" stroke="#fff" stroke-width="1.5"/></svg>
<p class="scroll-label">Scroll More</p>

<!-- about -->
<h2 class="about-title">ABOUT US</h2>
<a class="btn" style="left:221px;top:771px;width:157px">LEARN MORE <svg viewBox="0 0 18 14"><path d="M1 7h15M10 1l6 6-6 6" fill="none" stroke="#fff" stroke-width="1.6"/></svg></a>
<p class="about-copy">Lorem ipsum dolor sit amet consectetur. Quis sed consectetur nulla dictum non id amet aliquet diam. Hendrerit platea at sagittis arcu. Ultrices feugiat magna tellus morbi sed lectus odio elit. Dui nisl at sed nisl est id ultricies cursus. Nisi malesuada pharetra tellus tincidunt et mi lectus volutpat sapien.</p>

<!-- services -->
<div class="dotmap" role="img" aria-label="Faint dotted world map"></div>
<div class="services-panel"></div>
<h2 class="section-head" style="top:1027px"><span class="rule"></span>OUR SERVICES<span class="rule"></span></h2>
<p class="services-intro">Lorem ipsum dolor sit amet consectetur. Quis sed consectetur nulla dictum<br>non id amet aliquet diam. Hendrerit platea at sagittis arcu.</p>

<div class="photo" role="img" aria-label="Blue financial bar chart display" style="left:213px;top:1203px;background:radial-gradient(circle at 60% 40%,#3a8ff0,#0a2d8a 75%)"></div>
<div class="photo" role="img" aria-label="Tablet showing colourful charts" style="left:501px;top:1207px;background:radial-gradient(circle at 45% 45%,#f2f4f6,#c9d2dc 80%)"></div>
<div class="photo" role="img" aria-label="Desk with printed charts and calculator" style="left:797px;top:1209px;background:radial-gradient(circle at 50% 55%,#8fa6c4,#5a5d6a 85%)"></div>

<h3 class="service-title" style="left:181px;top:1415px">SERVICE 1</h3>
<h3 class="service-title" style="left:468px;top:1414px">SERVICE 2</h3>
<h3 class="service-title" style="left:766px;top:1415px">SERVICE 3</h3>
<p class="service-copy" style="left:185px;top:1453px">Lorem ipsum dolor sit amet consectetur. Quis sed consectetur nulla dictum non</p>
<p class="service-copy" style="left:479px;top:1451px">Lorem ipsum dolor sit amet consectetur. Quis sed consectetur nulla</p>
<p class="service-copy" style="left:766px;top:1444px">Lorem ipsum dolor sit amet consectetur. Quis sed consectetur nulla</p>
<a class="btn" style="left:237px;top:1549px;width:158px">LEARN MORE <svg viewBox="0 0 18 14"><path d="M1 7h15M10 1l6 6-6 6" fill="none" stroke="#fff" stroke-width="1.6"/></svg></a>
<a class="btn" style="left:527px;top:1549px;width:158px">LEARN MORE <svg viewBox="0 0 18 14"><path d="M1 7h15M10 1l6 6-6 6" fill="none" stroke="#fff" stroke-width="1.6"/></svg></a>
<a class="btn" style="left:837px;top:1549px;width:158px">LEARN MORE <svg viewBox="0 0 18 14"><path d="M1 7h15M10 1l6 6-6 6" fill="none" stroke="#fff" stroke-width="1.6"/></svg></a>

<!-- why work with us -->
<div class="contact-bg"></div>
<svg class="why" viewBox="0 1640 1200 910" width="1200" height="910">
  <defs>
    <linearGradient id="whyGrad" x1="0" y1="0" x2="0.3" y2="1">
      <stop offset="0" stop-color="#0a6fca"/>
      <stop offset="1" stop-color="#1c36a4"/>
    </linearGradient>
    <path id="card" d="M37.3,155.6 L63.5,264.5 A272,272 0 0 1 -63.5,264.5 L-37.3,155.6 A160,160 0 0 0 37.3,155.6 Z" fill="#fff" stroke="#fff" stroke-width="12" stroke-linejoin="round"/>
  </defs>
  <polygon points="0,1645 1200,1843 1200,2538 0,2308" fill="url(#whyGrad)"/>
  <path d="M499,1983 A117,117 0 0 0 733,1983" fill="none" stroke="#6fb6f0" stroke-width="2"/>
  <g fill="#ffffff">
    <circle cx="499" cy="1985" r="2.5"/><circle cx="517" cy="2049" r="3.5"/><circle cx="568" cy="2091" r="4"/>
    <circle cx="664" cy="2091" r="5"/><circle cx="714" cy="2049" r="3.5"/><circle cx="732" cy="1985" r="2.5"/>
  </g>
  <circle cx="616" cy="1983" r="80" fill="#0b1f5e" role="img" aria-label="Stock market chart on screen"/>

  <g transform="translate(616,1983)">
    <use href="#card" transform="rotate(72)"/>
    <use href="#card" transform="rotate(36)"/>
    <use href="#card"/>
    <use href="#card" transform="rotate(-36)"/>
    <use href="#card" transform="rotate(-72)"/>
  </g>

  <g fill="none" stroke="#0a6fca" stroke-width="2" stroke-linejoin="round" stroke-linecap="round">
    <!-- pie with bars -->
    <g transform="translate(404,2046)">
      <circle cx="4" cy="4" r="22"/><path d="M4,-18 V4 H26"/><path d="M-10,-2 v-10 M-4,-2 v-16"/><circle cx="16" cy="16" r="8" fill="#fff"/><path d="M16,11 v10"/>
    </g>
    <!-- document with handshake -->
    <g transform="translate(478,2146)">
      <rect x="-14" y="-22" width="28" height="34"/><path d="M-8,-14 h16 M-8,-7 h12 M-8,0 h8"/><path d="M-24,16 l10,8 l10,-6 l10,6 l14,-8"/>
    </g>
    <!-- report with calculator -->
    <g transform="translate(614,2194)">
      <rect x="-18" y="-24" width="28" height="42"/><circle cx="-4" cy="-12" r="7"/><rect x="0" y="-2" width="20" height="26" fill="#fff"/><path d="M4,5 h12 M4,11 h12 M4,17 h12"/>
    </g>
    <!-- hand with coin -->
    <g transform="translate(756,2150)">
      <circle cx="2" cy="-14" r="11"/><path d="M2,-20 v12"/><path d="M-26,22 l12,-12 h18 l-8,8 h14 l12,-10"/>
    </g>
    <!-- chart with magnifier -->
    <g transform="translate(824,2046)">
      <rect x="-20" y="-22" width="28" height="40"/><path d="M-14,-4 v-8 M-8,-4 v-12 M-2,-4 v-6"/><circle cx="10" cy="6" r="9" fill="#fff"/><path d="M16,13 l8,8"/>
    </g>
  </g>
</svg>
<h2 class="section-head" style="top:1832px;color:#fff"><span class="rule"></span>WHY WORK WITH US<span class="rule"></span></h2>

<p class="why-label" style="left:200px;top:2053px">LOREM IPSUM</p>
<p class="why-copy" style="left:200px;top:2085px">Lorem ipsum dolor sit amet consectetur. Lectus vitae.</p>
<p class="why-label" style="left:922px;top:2043px">LOREM IPSUM</p>
<p class="why-copy" style="left:922px;top:2075px">Lorem ipsum dolor sit amet consectetur. Lectus vitae.</p>
<p class="why-label" style="left:335px;top:2241px">LOREM IPSUM</p>
<p class="why-copy" style="left:335px;top:2273px">Lorem ipsum dolor sit amet consectetur. Lectus vitae.</p>
<p class="why-label" style="left:573px;top:2310px">LOREM IPSUM</p>
<p class="why-copy" style="left:573px;top:2342px">Lorem ipsum dolor sit amet consectetur. Lectus vitae.</p>
<p class="why-label" style="left:780px;top:2241px">LOREM IPSUM</p>
<p class="why-copy" style="left:780px;top:2273px">Lorem ipsum dolor sit amet consectetur. Lectus vitae.</p>

<!-- contact -->
<h2 class="contact-title">GET IN TOUCH</h2>
<p class="contact-copy">Lorem ipsum dolor sit amet consectetur. Mollis enim neque ut eget lacus. Nibh ut lacinia feugiat fermentum.</p>
<h3 class="contact-co">HARBORLINE ESTATE PARTNERS, LLC</h3>
<p class="info" style="top:2734px"><svg viewBox="0 0 18 18"><path d="M9 17s6-6 6-10a6 6 0 0 0-12 0c0 4 6 10 6 10z" fill="none" stroke="#222" stroke-width="1.5"/><circle cx="9" cy="7" r="2.2" fill="none" stroke="#222" stroke-width="1.5"/></svg>Your company address</p>
<p class="info" style="top:2765px"><svg viewBox="0 0 18 18"><rect x="1.5" y="3.5" width="15" height="11" fill="none" stroke="#222" stroke-width="1.5"/><path d="M1.5 4l7.5 6 7.5-6" fill="none" stroke="#222" stroke-width="1.5"/></svg>info@harborline.example</p>
<p class="info" style="top:2797px"><svg viewBox="0 0 18 18"><path d="M4 1.5l3 3.5-1.5 2.5c1 2 3 4 5 5l2.5-1.5 3.5 3-2 2.5C8 15.5 2.5 10 1.5 4z" fill="none" stroke="#222" stroke-width="1.5" stroke-linejoin="round"/></svg>745 55010 38</p>

<div class="field" style="left:577px;top:2552px;width:235px;height:42px">First name</div>
<div class="field" style="left:828px;top:2552px;width:234px;height:42px">Last name</div>
<div class="field" style="left:577px;top:2608px;width:235px;height:43px">Email</div>
<div class="field" style="left:828px;top:2608px;width:234px;height:43px">Phone number</div>
<div class="field" style="left:577px;top:2665px;width:485px;height:167px">Message</div>
<a class="btn" style="left:577px;top:2855px;width:147px;height:42px">SEND <svg viewBox="0 0 18 14"><path d="M1 7h15M10 1l6 6-6 6" fill="none" stroke="#fff" stroke-width="1.6"/></svg></a>

<!-- footer -->
<div class="footer-band"></div>
<footer class="footer">
  <p class="footer-about">Lorem ipsum dolor sit amet consectetur. Mollis enim neque ut eget lacus. Nibh ut lacinia feugiat fermentum.</p>
  <p class="footer-co">HARBORLINE ESTATE PARTNERS, LLC</p>
  <p class="footer-info" style="top:75px"><svg viewBox="0 0 18 18"><path d="M9 17s6-6 6-10a6 6 0 0 0-12 0c0 4 6 10 6 10z" fill="none" stroke="#fff" stroke-width="1.5"/><circle cx="9" cy="7" r="2.2" fill="none" stroke="#fff" stroke-width="1.5"/></svg>Your company address</p>
  <p class="footer-info" style="top:105px"><svg viewBox="0 0 18 18"><rect x="1.5" y="3.5" width="15" height="11" fill="none" stroke="#fff" stroke-width="1.5"/><path d="M1.5 4l7.5 6 7.5-6" fill="none" stroke="#fff" stroke-width="1.5"/></svg>info@harborline.example</p>
  <p class="footer-info" style="top:138px"><svg viewBox="0 0 18 18"><path d="M4 1.5l3 3.5-1.5 2.5c1 2 3 4 5 5l2.5-1.5 3.5 3-2 2.5C8 15.5 2.5 10 1.5 4z" fill="none" stroke="#fff" stroke-width="1.5" stroke-linejoin="round"/></svg>745 55010 38</p>
  <nav class="footer-nav">HOME<br>ABOUT<br>SERVICE<br>OUR CLIENTS<br>FAQ<br>CONTACT</nav>
  <span class="social" style="left:964px"></span>
  <span class="social" style="left:1005px"></span>
  <span class="social" style="left:1047px"></span>
  <div class="footer-rule"></div>
  <p class="copyright">© 2022 Harborline Estate Partners, LLC | All Rights Reserved</p>
</footer>

</body>
</html>
```